Online trading school - Website design

We are building an online trading school (trading of shares, commodities, indices, currencies). The purpose is to teach online traders how to trade successfully. We need to design the homepage of the website and logo (bramwelloq.com will be the domain). The homepage will contain the following elements

- logo
- Sign in and Register links/buttons
- upper menu
- short introduction
- a couple of bullet points 'Why to join our school?'
- sign up form
- text
- bottom menu

Attached is a draft for the designer. The draft is just for an inspiration, the actual structure of the website can be different if the designer thinks so.

The designer is free to choose colors.

School

3 page

```html
<!DOCTYPE html>
<html lang="en">
<head>
<meta charset="utf-8">
<title>bramwelloq.com — Online Trading School</title>
<link href="https://fonts.googleapis.com/css2?family=Raleway:ital,wght@0,400;0,500;0,600;0,700;1,400&display=swap" rel="stylesheet">
<style>
:root{
  --page:#eeeeee;
  --white:#ffffff;
  --red:#cc0000;
  --red-dark:#a30000;
  --red-soft:#e07b7b;
  --nav:#2a2b2d;
  --nav-line:#3d3e40;
  --grey-band:#aeb2b6;
  --grey-tab:#8e9296;
  --text:#444444;
  --text-dark:#222222;
  --footer:#222327;
  --search-btn:#3a8fc2;
  --border:#d8d8d8;
}
*{box-sizing:border-box;margin:0;padding:0}
html,body{width:1200px;height:1136px;overflow:hidden}
body{background:var(--page);font-family:'Raleway',sans-serif;color:var(--text);position:relative}
.topbar{position:absolute;left:0;top:0;width:1200px;height:46px;border-bottom:1px solid #dcdcdc}
.account{position:absolute;right:126px;top:16px;display:flex;gap:24px;font-size:13px}
.account a{text-decoration:none;display:flex;align-items:center;gap:5px}
.account .register{color:#777}
.account .signin{color:var(--red)}
.brand{position:absolute;left:124px;top:62px;font-size:18px;font-weight:700;color:var(--red)}
.social{position:absolute;left:970px;top:63px;display:flex;gap:6px}
.social span{width:31px;height:31px;border-radius:50%;background:#9a9ea3;display:block}
.panel{position:absolute;background:var(--white);border:1px solid var(--border);border-radius:3px}
.hero-panel{left:125px;top:117px;width:950px;height:334px;padding:4px}
.mainnav{height:44px;background:var(--nav);display:flex;align-items:center}
.mainnav a{height:44px;display:flex;align-items:center;padding:0 18px;color:#ddd;font-size:13px;text-decoration:none;border-right:1px solid var(--nav-line);text-transform:uppercase}
.mainnav a.active{color:var(--red);padding:0 20px 0 26px}
.search{margin-left:7px;display:flex;width:267px;height:32px}
.search span{flex:1;background:#444548;color:#8c8c8c;font-style:italic;font-size:13px;padding:8px 0 0 37px}
.search b{width:45px;background:var(--search-btn);display:flex;align-items:center;justify-content:center}
.hero{position:relative;height:282px;background:linear-gradient(90deg,#f3ede7 0%,#f1d9c6 40%,#c8a27f 55%,#8a8d93 75%,#5d6067 100%)}
.hero h1{position:absolute;left:40px;top:114px;font-size:24px;font-weight:400;color:var(--red)}
.hero p{position:absolute;left:40px;top:149px;font-size:13px;font-weight:600;color:var(--text-dark);line-height:18px}
.btn{position:absolute;left:40px;top:196px;background:var(--red);color:#fff;font-size:14px;padding:9px 13px;text-decoration:none}
.photo-area{position:absolute}
.band{position:absolute;height:39px;display:flex;align-items:center}
.band .tab{width:43px;height:39px;display:flex;align-items:center;justify-content:center}
.band h2{font-size:13px;font-weight:600;text-transform:uppercase}
.why{left:125px;top:462px;width:551px;height:304px}
.why .band{left:5px;top:4px;width:540px;background:var(--grey-band)}
.why .band .tab{background:var(--grey-tab)}
.why .band h2{color:#fff;margin-left:15px}
.why ul{position:absolute;left:44px;top:66px;list-style:none}
.why li{display:flex;align-items:center;gap:8px;font-size:14px;height:36px;color:var(--text)}
.join{position:absolute;left:688px;top:463px;width:386px;height:302px;background:var(--red);border-radius:2px}
.join .band{left:5px;top:5px;width:376px;background:#fff}
.join .band .tab{background:var(--red-soft)}
.join .band h2{color:var(--red-soft);margin-left:17px;font-weight:500}
.field{position:absolute;left:47px;width:217px;height:36px;border:1px solid #f08a8a;color:#fff;font-style:italic;font-size:13px;padding:10px 14px}
.agree{position:absolute;left:48px;top:214px;color:#fff;font-style:italic;font-size:14px;display:flex;align-items:center;gap:5px}
.agree i{width:15px;height:15px;border-radius:50%;background:#f2dede;border:4px solid #e9e9e9;display:block;box-shadow:inset 0 0 0 2px var(--red-dark)}
.submit{position:absolute;left:49px;top:245px;width:99px;height:35px;background:var(--red-dark);color:#fff;font-size:14px;display:flex;align-items:center;justify-content:center}
.offers{left:125px;top:778px;width:951px;height:224px}
.offers .band{left:5px;top:4px;width:939px;background:var(--grey-band)}
.offers .band .tab{background:var(--grey-band);border-right:1px solid #c4c7ca}
.offers .band h2{color:#fff;flex:1;text-align:center;margin-right:43px}
.offers p{position:absolute;left:439px;top:76px;width:480px;font-size:13px;line-height:21px;color:#555}
.offers p a{color:var(--red);font-weight:600;text-decoration:none;margin-left:6px}
.site-footer{position:absolute;left:0;top:1024px;width:1200px;height:112px;background:var(--footer);color:#eee;text-align:center}
.site-footer nav{margin-top:34px;font-style:italic;font-size:14px}
.site-footer nav span{margin:0 16px}
.site-footer small{display:block;margin-top:17px;font-size:14px}
</style>
</head>
<body>
<header class="topbar">
  <div class="account">
    <a class="register" href="#"><svg width="13" height="16" viewBox="0 0 13 16"><rect x="1" y="7" width="11" height="8" fill="#aaa"/><path d="M3 7V4.5a3.5 3.5 0 0 1 7 0V7" fill="none" stroke="#aaa" stroke-width="1.6"/></svg>Register</a>
    <a class="signin" href="#"><svg width="17" height="17" viewBox="0 0 17 17"><circle cx="8.5" cy="8.5" r="7" fill="none" stroke="#cc0000" stroke-width="1.6"/><path d="M2 8.5h8M7 5.5l3 3-3 3" fill="none" stroke="#cc0000" stroke-width="1.6"/></svg>Sign in now</a>
  </div>
</header>
<div class="brand">BRAMWELLOQ.COM</div>
<div class="social" aria-label="Social links"><span></span><span></span><span></span></div>

<section class="panel hero-panel">
  <nav class="mainnav">
    <a class="active" href="#">About our school</a>
    <a href="#">Risk warning</a>
    <a href="#" style="padding:0 27px">FAQ</a>
    <a href="#">Trading glossary</a>
    <a href="#">Contact</a>
    <div class="search"><span>Search Web and Directory</span><b><svg width="18" height="18" viewBox="0 0 18 18"><circle cx="7.5" cy="7.5" r="5.5" fill="none" stroke="#fff" stroke-width="1.8"/><path d="M11.5 11.5l5 5" stroke="#fff" stroke-width="1.8"/></svg></b></div>
  </nav>
  <div class="hero">
    <div class="photo-area" role="img" aria-label="Students working on laptops at a desk, seen from above" style="left:370px;top:0;width:572px;height:282px;background:linear-gradient(90deg,rgba(200,160,120,0) 0%,rgba(120,120,125,.35) 50%,rgba(80,82,88,.5) 100%)"></div>
    <h1>we are an online trading school.</h1>
    <p>we teach trading of shares, commodities,<br>indices, currencies</p>
    <a class="btn" href="#">Learn More ›</a>
  </div>
</section>

<section class="panel why">
  <div class="band"><div class="tab"><svg width="10" height="16" viewBox="0 0 10 16"><path d="M2 2l6 6-6 6" fill="none" stroke="#fff" stroke-width="2"/></svg></div><h2>Why to join us?</h2></div>
  <ul>
    <li><svg width="22" height="22" viewBox="0 0 22 22"><circle cx="10" cy="12" r="9" fill="none" stroke="#666" stroke-width="1.6"/><path d="M5 12l4 4 10-14" fill="none" stroke="#666" stroke-width="2"/></svg>Best trading tips ever</li>
    <li><svg width="22" height="22" viewBox="0 0 22 22"><circle cx="10" cy="12" r="9" fill="none" stroke="#666" stroke-width="1.6"/><path d="M5 12l4 4 10-14" fill="none" stroke="#666" stroke-width="2"/></svg>Secret tips from expets</li>
    <li><svg width="22" height="22" viewBox="0 0 22 22"><circle cx="10" cy="12" r="9" fill="none" stroke="#666" stroke-width="1.6"/><path d="M5 12l4 4 10-14" fill="none" stroke="#666" stroke-width="2"/></svg>We teach you how to trade online</li>
    <li><svg width="22" height="22" viewBox="0 0 22 22"><circle cx="10" cy="12" r="9" fill="none" stroke="#666" stroke-width="1.6"/><path d="M5 12l4 4 10-14" fill="none" stroke="#666" stroke-width="2"/></svg>Learn how to trade commodities</li>
    <li><svg width="22" height="22" viewBox="0 0 22 22"><circle cx="10" cy="12" r="9" fill="none" stroke="#666" stroke-width="1.6"/><path d="M5 12l4 4 10-14" fill="none" stroke="#666" stroke-width="2"/></svg>Learn how to become a trader</li>
  </ul>
  <div class="photo-area" role="img" aria-label="Smiling student holding a laptop and books" style="left:298px;top:58px;width:250px;height:244px;background:linear-gradient(180deg,#eef0f3 0%,#c9ced6 50%,#2c3e73 100%);opacity:.85"></div>
</section>

<section class="join">
  <div class="photo-area" role="img" aria-label="Group of cheering students" style="left:225px;top:50px;width:161px;height:252px;background:linear-gradient(180deg,#c40000,#8e1010)"></div>
  <div class="band"><div class="tab"><svg width="10" height="16" viewBox="0 0 10 16"><path d="M2 2l6 6-6 6" fill="none" stroke="#fff" stroke-width="2"/></svg></div><h2>Join our school now!</h2></div>
  <div class="field" style="top:66px">First name</div>
  <div class="field" style="top:116px">Last name</div>
  <div class="field" style="top:165px">Email</div>
  <div class="agree"><i></i>Agree with our terms and Conditions</div>
  <div class="submit">SUBMIT</div>
</section>

<section class="panel offers">
  <div class="band"><div class="tab"><svg width="10" height="16" viewBox="0 0 10 16"><path d="M2 2l6 6-6 6" fill="none" stroke="#fff" stroke-width="2"/></svg></div><h2>What do we offers?</h2></div>
  <div class="photo-area" role="img" aria-label="Group of students sitting together on a bench with laptops and tablets" style="left:21px;top:55px;width:389px;height:156px;background:linear-gradient(90deg,#5b4a3a,#a88b63 50%,#6e6a58)"></div>
  <p>Lorem ipsum dolor sit amet, consectetur adipisicing elit, sed do eiusmod tempor incididunt ut labore et dolore magna aliqua. Ut enim ad minim veniam, quis nostrud exercitation ullamco laboris nisi ut aliquip ex ea commodo consequat. Duis aute irure dolor in reprehenderit in voluptate velit esse cillum dolore eu fugiat .... <a href="#">READ MORE&gt;</a></p>
</section>

<footer class="site-footer">
  <nav>Terms and conditions<span>|</span>Privacy Protection</nav>
  <small>@Copyright 2016. All right reserved by the Company.</small>
</footer>
</body>
</html>
```